Mission Statement Board for front lobby

We need a mission statement board for our front lobby at our company called PatternForge. We are a web content management company that builds websites for our clients. We would like two boards, same size, canvas material (not thin poster board or anything like that) size H 3' x L 2', white background, blue and black colored font, our logo on top in blue/gray/black and some blue coloring around top and bottom, kind of framing the white background. Please reference our very rough draft we did in Word so you get an idea of what we're thinking- the attachment shows what we would like on each board. Reference our website to see logo and fonts if you would like, please keep the board similar to our fonts and colors. www.patternforge-example.com

Contact info: Donna Whitlock
Email: donna.whitlock@patternforge-example.com
Phone: 555-217-4039
Updates

Please do not include in a design my contact info, no email donna.whitlock@patternforge-example.com, no phone # 555-217-4039. I added that info to the project when I posted it, but it is not part of the design.... reference attachment posted in project with exactly what we want.

Target Market(s)

Clients & employees in the office who will see the boards in lobby

Industry/Entity Type

It Company

Font styles to use
Other font styles liked:
• reference attachment (but font is flexible within reason)

Colors
33a6d7
0255a3
eaf1f7
0292cd
85cae6
cee9f5
000000
5c5c5c
959595

Requirements
Must have
• Needs to be a professional sign that hangs on wall, company logo, cohesive colors and fonts
Nice to have
• Get creative with the border/framing around the white background
Should not have
• Unprofessional fonts, typos, thin cheap looking poster board materal.

```html
<!DOCTYPE html>
<html lang="en">
<head>
<meta charset="utf-8">
<title>PatternForge – Core Values Lobby Boards</title>
<link rel="stylesheet" href="https://fonts.googleapis.com/css2?family=Oswald:wght@300;400;600&family=Lato:wght@400;700&display=swap">
<style>
  :root {
    --stage: #9b9b9b;
    --label: #e4e4e4;
    --navy: #0255a3;
    --ocean: #0292cd;
    --sky: #33a6d7;
    --mist: #85cae6;
    --ice: #cee9f5;
    --frost: #eaf1f7;
    --ink: #111111;
    --charcoal: #454545;
    --slate: #5c5c5c;
    --ash: #959595;
    --paper: #ffffff;
    --panel-blue: #a5cbe8;
  }
  html, body {
    margin: 0;
    padding: 0;
    width: 1200px;
    height: 1200px;
    overflow: hidden;
    background: var(--stage);
  }
  .stage {
    position: relative;
    width: 1200px;
    height: 1200px;
  }
  .variant-label {
    position: absolute;
    top: 140px;
    margin: 0;
    font-family: "Oswald", sans-serif;
    font-weight: 600;
    font-size: 50px;
    letter-spacing: 1px;
    color: var(--label);
    transform: translateX(-50%);
    white-space: nowrap;
  }
  .variant-label--one { left: 320px; }
  .variant-label--two { left: 890px; }
  .board {
    position: absolute;
    top: 230px;
    width: 534px;
    height: 800px;
    display: block;
  }
  .board--split { left: 56px; }
  .board--wave { left: 622px; }
  .core-title {
    font-family: "Oswald", sans-serif;
    font-weight: 400;
    font-size: 40px;
    text-anchor: middle;
  }
  .value-title {
    font-family: "Oswald", sans-serif;
    font-weight: 400;
    font-size: 25px;
    text-anchor: middle;
  }
  .value-body {
    font-family: "Lato", sans-serif;
    font-size: 13px;
    text-anchor: middle;
  }
  .mission-title {
    font-family: "Oswald", sans-serif;
    font-weight: 300;
    font-size: 39px;
    text-anchor: middle;
    fill: var(--charcoal);
  }
  .mission-title .accent { fill: var(--navy); font-weight: 400; }
  .mission-body {
    font-family: "Lato", sans-serif;
    font-size: 17px;
    text-anchor: middle;
    fill: var(--ink);
  }
  .mission-body .lead { font-weight: 700; }
  .brand-name {
    font-family: "Oswald", sans-serif;
    font-weight: 400;
    font-size: 30px;
    text-anchor: middle;
    fill: var(--navy);
  }
  .on-dark { fill: var(--paper); }
  .on-light { fill: var(--ink); }
  .defs-holder { position: absolute; width: 0; height: 0; }
</style>
</head>
<body>
<main class="stage">

  <svg class="defs-holder" aria-hidden="true">
    <defs>
      <symbol id="hex" viewBox="-1 -1 2 2">
        <polygon points="0,-1 0.866,-0.5 0.866,0.5 0,1 -0.866,0.5 -0.866,-0.5"/>
      </symbol>
      <clipPath id="split-left"><rect x="0" y="0" width="333" height="1000"/></clipPath>
      <clipPath id="split-right"><rect x="333" y="0" width="334" height="1000"/></clipPath>
      <linearGradient id="wave-deep" x1="0" y1="0" x2="1" y2="0">
        <stop offset="0" stop-color="#33a6d7"/>
        <stop offset="1" stop-color="#0292cd"/>
      </linearGradient>
    </defs>
  </svg>

  <h2 class="variant-label variant-label--one">DESIGN - 01</h2>
  <h2 class="variant-label variant-label--two">DESIGN - 02</h2>

  <!-- Split panel board -->
  <svg class="board board--split" viewBox="0 0 667 1000" role="img" aria-label="PatternForge core values board, split charcoal and blue">
    <rect class="panel-dark" x="0" y="0" width="333" height="746" fill="#474747"/>
    <rect class="panel-blue" x="333" y="0" width="334" height="746" fill="#a5cbe8"/>
    <rect class="mission-area" x="0" y="746" width="667" height="242" fill="#fafafa"/>
    <rect x="0" y="988" width="333" height="12" fill="#474747"/>
    <rect x="333" y="988" width="334" height="12" fill="#a5cbe8"/>

    <g class="core-title">
      <text x="317" y="81" class="on-dark" clip-path="url(#split-left)">OUR CORE VALUES</text>
      <text x="317" y="81" fill="#2b2b2b" clip-path="url(#split-right)">OUR CORE VALUES</text>
    </g>

    <g class="hex-field">
      <use href="#hex" x="53" y="201" width="50" height="50" fill="#8a8a8a" opacity=".8"/>
      <use href="#hex" x="51" y="208" width="24" height="24" fill="#b5b5b5" opacity=".8"/>
      <use href="#hex" x="215" y="223" width="60" height="60" fill="#555" opacity=".8"/>
      <use href="#hex" x="92" y="198" width="190" height="190" fill="#3a3a3a" opacity=".9"/>
      <use href="#hex" x="43" y="398" width="50" height="50" fill="#9c9c9c"/>
      <use href="#hex" x="117" y="402" width="36" height="36" fill="#a9a9a9"/>
      <use href="#hex" x="140" y="373" width="80" height="80" fill="#333"/>
      <use href="#hex" x="68" y="473" width="240" height="240" fill="#363636" opacity=".95"/>
      <use href="#hex" x="58" y="665" width="40" height="40" fill="#7a7a7a"/>
      <use href="#hex" x="158" y="673" width="100" height="100" fill="#8a8a8a" opacity=".7"/>
      <use href="#hex" x="290" y="518" width="50" height="50" fill="#7a7a7a" opacity=".7"/>

      <use href="#hex" x="304" y="143" width="200" height="200" fill="#2f74b7" opacity=".75"/>
      <use href="#hex" x="314" y="153" width="180" height="180" fill="#1d5fa3" opacity=".85"/>
      <use href="#hex" x="483" y="175" width="20" height="20" fill="#7a8c99"/>
      <use href="#hex" x="497" y="207" width="66" height="66" fill="#5b7f9b" opacity=".85"/>
      <use href="#hex" x="562" y="193" width="40" height="40" fill="#5aa7dc"/>
      <use href="#hex" x="527" y="250" width="36" height="36" fill="#43aeea"/>
      <use href="#hex" x="425" y="298" width="50" height="50" fill="#6aa0c2" opacity=".7"/>
      <use href="#hex" x="430" y="298" width="210" height="210" fill="#1f8ae0" opacity=".95"/>
      <use href="#hex" x="574" y="308" width="36" height="36" fill="#4b7ea6" opacity=".7"/>
      <use href="#hex" x="361" y="516" width="224" height="224" fill="#3a97db" opacity=".95"/>
      <use href="#hex" x="565" y="562" width="70" height="70" fill="#5aaee0" opacity=".8"/>
      <use href="#hex" x="549" y="558" width="30" height="30" fill="#2d7fb8" opacity=".6"/>
      <use href="#hex" x="547" y="666" width="38" height="38" fill="#6a8fa8" opacity=".7"/>
      <use href="#hex" x="593" y="706" width="16" height="16" fill="#2a7fa0"/>
      <use href="#hex" x="305" y="695" width="96" height="96" fill="#3a85b0" opacity=".7"/>
      <use href="#hex" x="345" y="703" width="60" height="60" fill="#2f7ba5" opacity=".6"/>
    </g>

    <g class="brand-mark">
      <use href="#hex" x="217" y="315" width="236" height="236" fill="#ffffff" stroke="#0255a3" stroke-width=".035"/>
      <circle cx="335" cy="390" r="14" fill="#0255a3"/>
      <text class="brand-name" x="335" y="460">PatternForge</text>
    </g>

    <g class="value value--accountability">
      <text class="value-title on-dark" x="192" y="290">ACCOUNTABILITY</text>
      <text class="value-body on-dark"><tspan x="192" y="307">Taking responsibility for</tspan><tspan x="192" y="323">one’s own actions.</tspan></text>
    </g>
    <g class="value value--respect">
      <text class="value-title on-dark" x="401" y="217">RESPECT</text>
      <text class="value-body on-dark"><tspan x="404" y="236">Understand and value</tspan><tspan x="404" y="252">differences in others.</tspan><tspan x="404" y="268">Listen thoughtfully to</tspan><tspan x="404" y="284">understand.</tspan></text>
    </g>
    <g class="value value--excellence">
      <text class="value-title on-dark" x="530" y="389">EXCELLENCE</text>
      <text class="value-body on-dark"><tspan x="532" y="407">We continually improve our</tspan><tspan x="532" y="423">standards and processes so</tspan><tspan x="532" y="439">that excellence simple</tspan><tspan x="532" y="455">becomes a natural</tspan><tspan x="532" y="471">consequence of our work.</tspan></text>
    </g>
    <g class="value value--loyalty">
      <text class="value-title on-dark" x="187" y="560">LOYALTY</text>
      <text class="value-body on-dark"><tspan x="193" y="588">Working collaboratively with</tspan><tspan x="193" y="604">PatternForge employees,</tspan><tspan x="193" y="620">partners and customers to</tspan><tspan x="193" y="636">solve problems and achieve</tspan><tspan x="193" y="652">goals.</tspan></text>
    </g>
    <g class="value value--integrity">
      <text class="value-title on-dark" x="470" y="596">INTERGRITY</text>
      <text class="value-body on-dark"><tspan x="471" y="614">We believe that to be</tspan><tspan x="471" y="630">successful, it is essential</tspan><tspan x="471" y="646">to operate at the highest</tspan><tspan x="471" y="662">levels of honesty,</tspan><tspan x="471" y="678">responsibility and trust.</tspan></text>
    </g>

    <g class="mission">
      <text class="mission-title" x="334" y="845"><tspan class="accent">OUR</tspan> MISSION STATEMENT:</text>
      <text class="mission-body"><tspan x="334" y="868">We design and implement extraordinary web solutions</tspan><tspan x="334" y="889">to help our clients achieve their goals.</tspan><tspan class="lead" x="334" y="917">Our Faith...</tspan><tspan x="334" y="938">We reflect the love of Christ in us and through us</tspan><tspan x="334" y="959">to our fellow employees, partners and clients.</tspan></text>
    </g>
  </svg>

  <!-- Wave frame board -->
  <svg class="board board--wave" viewBox="0 0 667 1000" role="img" aria-label="PatternForge core values board, white with blue wave frame">
    <rect x="0" y="0" width="667" height="1000" fill="#ffffff"/>
    <path class="wave wave--light" d="M0,0 H667 V158 C540,70 360,20 0,60 Z" fill="#85cae6"/>
    <path class="wave wave--mid" d="M0,0 H667 V105 C540,40 360,10 0,90 Z" fill="#4fb6e2" opacity=".85"/>
    <path class="wave wave--deep" d="M0,0 H667 V55 C470,10 200,20 0,128 Z" fill="url(#wave-deep)"/>
    <rect x="0" y="983" width="333" height="17" fill="#85cae6"/>
    <rect x="333" y="983" width="334" height="17" fill="#0292cd"/>

    <text class="core-title" x="319" y="113" fill="#111">OUR CORE VALUES</text>

    <g class="hex-field">
      <use href="#hex" x="65" y="200" width="50" height="50" fill="#5b9bd1" opacity=".85"/>
      <use href="#hex" x="52" y="209" width="24" height="24" fill="#8fb0c6" opacity=".8"/>
      <use href="#hex" x="92" y="198" width="190" height="190" fill="#bcd8e8" opacity=".9"/>
      <use href="#hex" x="214" y="223" width="60" height="60" fill="#9fd3ec" opacity=".8"/>
      <use href="#hex" x="43" y="398" width="50" height="50" fill="#6fa3bd" opacity=".85"/>
      <use href="#hex" x="116" y="402" width="36" height="36" fill="#9cc8e0"/>
      <use href="#hex" x="140" y="375" width="80" height="80" fill="#6f9fcc" opacity=".9"/>
      <use href="#hex" x="52" y="453" width="260" height="260" fill="#b5d6e8" opacity=".7"/>
      <use href="#hex" x="42" y="468" width="230" height="230" fill="#8fb8cc" opacity=".85"/>
      <use href="#hex" x="59" y="667" width="36" height="36" fill="#a8dcf2"/>
      <use href="#hex" x="124" y="640" width="70" height="70" fill="#c8e4f2" opacity=".8"/>
      <use href="#hex" x="274" y="640" width="50" height="50" fill="#5a9fc4" opacity=".85"/>
      <use href="#hex" x="290" y="518" width="50" height="50" fill="#cde9f6" opacity=".8"/>

      <use href="#hex" x="304" y="143" width="200" height="200" fill="#a4d2ea" opacity=".8"/>
      <use href="#hex" x="314" y="153" width="180" height="180" fill="#6fb0d6" opacity=".85"/>
      <use href="#hex" x="482" y="179" width="20" height="20" fill="#8fa5b4"/>
      <use href="#hex" x="505" y="221" width="44" height="44" fill="#cde7f2"/>
      <use href="#hex" x="562" y="193" width="40" height="40" fill="#4aa9df"/>
      <use href="#hex" x="526" y="250" width="36" height="36" fill="#5ab8e6"/>
      <use href="#hex" x="422" y="298" width="220" height="220" fill="#95cfec" opacity=".7"/>
      <use href="#hex" x="432" y="308" width="200" height="200" fill="#6dbfe6" opacity=".75"/>
      <use href="#hex" x="573" y="308" width="36" height="36" fill="#5aa7cf" opacity=".7"/>
      <use href="#hex" x="367" y="508" width="230" height="230" fill="#85c9ea" opacity=".7"/>
      <use href="#hex" x="377" y="518" width="210" height="210" fill="#4aa9df" opacity=".85"/>
      <use href="#hex" x="567" y="563" width="70" height="70" fill="#5ab8e6" opacity=".8"/>
      <use href="#hex" x="548" y="663" width="36" height="36" fill="#4d91b8" opacity=".7"/>
      <use href="#hex" x="592" y="706" width="16" height="16" fill="#4a8fb0"/>
      <use href="#hex" x="302" y="693" width="100" height="100" fill="#3b88b5" opacity=".75"/>
      <use href="#hex" x="342" y="698" width="60" height="60" fill="#2f7ba5" opacity=".65"/>
      <use href="#hex" x="290" y="520" width="50" height="50" fill="#bfe6f7" opacity=".7"/>
    </g>

    <g class="brand-mark">
      <use href="#hex" x="217" y="315" width="236" height="236" fill="#ffffff" stroke="#0292cd" stroke-width=".03"/>
      <circle cx="335" cy="390" r="14" fill="#0255a3"/>
      <text class="brand-name" x="335" y="460">PatternForge</text>
    </g>

    <g class="value value--accountability">
      <text class="value-title on-light" x="192" y="296">ACCOUNTABILITY</text>
      <text class="value-body on-light"><tspan x="192" y="315">Taking responsibility for</tspan><tspan x="192" y="331">one’s own actions.</tspan></text>
    </g>
    <g class="value value--respect">
      <text class="value-title on-light" x="408" y="217">RESPECT</text>
      <text class="value-body on-light"><tspan x="409" y="236">Understand and value</tspan><tspan x="409" y="252">differences in others.</tspan><tspan x="409" y="268">Listen thoughtfully to</tspan><tspan x="409" y="284">understand.</tspan></text>
    </g>
    <g class="value value--excellence">
      <text class="value-title on-light" x="537" y="378">EXCELLENCE</text>
      <text class="value-body on-light"><tspan x="537" y="397">We continually improve our</tspan><tspan x="537" y="413">standards and processes so</tspan><tspan x="537" y="429">that excellence simple</tspan><tspan x="537" y="445">becomes a natural</tspan><tspan x="537" y="461">consequence of our work.</tspan></text>
    </g>
    <g class="value value--loyalty">
      <text class="value-title on-light" x="161" y="563">LOYALTY</text>
      <text class="value-body on-light"><tspan x="158" y="585">Working collaboratively with</tspan><tspan x="158" y="601">PatternForge employees,</tspan><tspan x="158" y="617">partners and customers to</tspan><tspan x="158" y="633">solve problems and achieve</tspan><tspan x="158" y="649">goals.</tspan></text>
    </g>
    <g class="value value--integrity">
      <text class="value-title on-light" x="488" y="594">INTERGRITY</text>
      <text class="value-body on-light"><tspan x="483" y="616">We believe that to be successful,</tspan><tspan x="483" y="632">it is essential to operate at the</tspan><tspan x="483" y="648">highest levels of honesty,</tspan><tspan x="483" y="664">responsibility and trust.</tspan></text>
    </g>

    <g class="mission">
      <text class="mission-title" x="334" y="845"><tspan class="accent">OUR</tspan> MISSION STATEMENT:</text>
      <text class="mission-body"><tspan x="334" y="868">We design and implement extraordinary web solutions</tspan><tspan x="334" y="889">to help our clients achieve their goals.</tspan><tspan class="lead" x="334" y="917">Our Faith...</tspan><tspan x="334" y="938">We reflect the love of Christ in us and through us</tspan><tspan x="334" y="959">to our fellow employees, partners and clients.</tspan></text>
    </g>
  </svg>

</main>
</body>
</html>
```